Tall Gum Equipment Hire Business Card Design

Tall Gum Equipment Hire Pty Ltd

WET or DRY HIRE

Kestrel M5-8 + attachments
Turf Cutter
Lawn mowers with catchers
Brushcutters
Blowers

We require a business card with the above information for a new equipment hire Company. Would like to see a redish/brown background or something to do with an Australian Red Dog (Cattle Dog) on the business card as our Logo - even some sort of watermark as a background.

Industry/Entity Type

Business

Contact Information for Business Card

ABN: 81 207 935 316
17B Moller Road Emerald Qld 4720
PO Box 8157 Emerald Qld 4720
PH: 0413072846 or 0437150928
Email: sunvale.turf@quollnet.example

```html
<!DOCTYPE html>
<html lang="en">
<head>
<meta charset="utf-8">
<title>Tall Gum Equipment Hire – Business Card</title>
<link rel="stylesheet" href="https://fonts.googleapis.com/css2?family=Quicksand:wght@400&family=Open+Sans:wght@400&display=swap">
<style>
  :root {
    --page-bg: #f4f4f4;
    --card-top: #a5302a;
    --card-bottom: #5b1f17;
    --brand-silver: #d9d9d9;
    --contact-text: #ffffff;
    --icon-fill: #e6e6e6;
  }
  * { box-sizing: border-box; margin: 0; padding: 0; }
  html, body {
    width: 1200px;
    height: 900px;
    overflow: hidden;
    background: var(--page-bg);
  }
  .business-card {
    position: absolute;
    left: 160px;
    top: 180px;
    width: 880px;
    height: 540px;
    border-radius: 42px;
    background: linear-gradient(180deg, var(--card-top) 0%, var(--card-bottom) 100%);
    overflow: hidden;
  }
  .brand-name {
    position: absolute;
    left: 66px;
    top: 120px;
    font-family: "Quicksand", sans-serif;
    font-weight: 400;
    color: var(--brand-silver);
  }
  .brand-name__main {
    display: block;
    font-size: 104px;
    line-height: 1;
    letter-spacing: 1px;
  }
  .brand-name__sub {
    display: block;
    margin-top: 4px;
    font-size: 26px;
    letter-spacing: 3px;
  }
  .contact-list {
    position: absolute;
    left: 76px;
    top: 358px;
    list-style: none;
    font-family: "Open Sans", sans-serif;
    font-weight: 400;
    color: var(--contact-text);
  }
  .contact-list__item {
    display: flex;
    align-items: center;
    gap: 10px;
    font-size: 22px;
    line-height: 29px;
  }
  .contact-list__icon {
    width: 24px;
    height: 22px;
    fill: var(--icon-fill);
    flex: none;
  }
  .contact-list__item--abn {
    padding-left: 34px;
    font-size: 18px;
    line-height: 26px;
  }
</style>
</head>
<body>
  <main class="business-card">
    <h1 class="brand-name">
      <span class="brand-name__main">Tall Gum</span>
      <span class="brand-name__sub">Equipment Hire Pty Ltd</span>
    </h1>

    <ul class="contact-list">
      <li class="contact-list__item">
        <svg class="contact-list__icon" viewBox="0 0 24 22" aria-hidden="true"><path d="M12 1 1 11h3v10h6v-6h4v6h6V11h3z"/></svg>
        17B Moller Road Emerald Qld 4720
      </li>
      <li class="contact-list__item">
        <svg class="contact-list__icon" viewBox="0 0 24 22" aria-hidden="true"><path d="M12 1 1 11h3v10h6v-6h4v6h6V11h3z"/></svg>
        PO Box 8157 Emerald Qld 4720
      </li>
      <li class="contact-list__item">
        <svg class="contact-list__icon" viewBox="0 0 24 22" aria-hidden="true"><path d="M5 2c1-1 2-1 3 0l2 3c.6 1 .4 2-.4 2.6L8.3 8.8c1 2.4 2.8 4.3 5.2 5.4l1.3-1.3c.7-.7 1.7-.8 2.5-.2l3 2c1 .7 1 1.8.2 2.7l-1.6 1.6c-1.2 1.2-3 1.4-4.6.7C8.2 17.4 4.5 13.7 2.3 9 1.6 7.4 1.8 5.6 3 4.4z"/></svg>
        0413072846
      </li>
      <li class="contact-list__item">
        <svg class="contact-list__icon" viewBox="0 0 24 22" aria-hidden="true"><path d="M5 2c1-1 2-1 3 0l2 3c.6 1 .4 2-.4 2.6L8.3 8.8c1 2.4 2.8 4.3 5.2 5.4l1.3-1.3c.7-.7 1.7-.8 2.5-.2l3 2c1 .7 1 1.8.2 2.7l-1.6 1.6c-1.2 1.2-3 1.4-4.6.7C8.2 17.4 4.5 13.7 2.3 9 1.6 7.4 1.8 5.6 3 4.4z"/></svg>
        0437150928
      </li>
      <li class="contact-list__item">
        <svg class="contact-list__icon" viewBox="0 0 24 22" aria-hidden="true"><path d="M2 7 12 1l10 6v13H2zm2 1.5V18h16V8.5l-8 5.5z"/></svg>
        sunvale.turf@quollnet.example
      </li>
      <li class="contact-list__item contact-list__item--abn">ABN: 81 207 935 316</li>
    </ul>
  </main>
</body>
</html>
```